Business card and (possibly) logo

Hi - we need a new business card.
We have an existing logo that we quite like but we are open to options.
We are an architectural firm - we specialize in upmarket residential work and apartment blocks.
We are chasing a business card at present but also want to extensively update our website going forward to attract a much higher level of client / investor / developer.
Our current logo is black, grey and yellow and based on the sun/moon temples in Mexico.
We are open to variations.
We want to communicate professionalism, trust, quality.
Our website is www.corvelldesignhouse.com.au - but note as above - we want to change the website as well to be a lot 'classier' and to appeal to a higher end market.

thanks

Target Market(s)

We are an architect firm - our target market is Developers and builders of high end houses and luxury apartment blocks. Also private home owners wanting to build excellent expensive houses. (ideally over $1m budgets)

Industry/Entity Type

Residential

Requirements
Must have
• Logo
Contact details;
Name
phone, mobile, email, web

```html
<!DOCTYPE html>
<html lang="en">
<head>
<meta charset="utf-8">
<title>Corvell Design House — Business Card</title>
<link href="https://fonts.googleapis.com/css2?family=Russo+One&display=swap" rel="stylesheet">
<style>
  :root {
    --backdrop: #1d2023;
    --backdrop-light: #2a2e31;
    --card-grey-light: #e4e4e4;
    --card-grey: #a9a9a9;
    --brand-orange: #dc832a;
    --ink-dark: #2a2424;
    --band-light: #c9c9c9;
    --band-dark: #7d7b7a;
    --text-light: #ffffff;
  }
  * { margin: 0; padding: 0; box-sizing: border-box; }
  html, body {
    width: 1200px;
    height: 853px;
    overflow: hidden;
  }
  body {
    position: relative;
    background: radial-gradient(ellipse at 40% 55%, var(--backdrop-light), var(--backdrop) 70%);
    font-family: "Russo One", sans-serif;
  }
  .card {
    position: absolute;
    width: 595px;
    height: 358px;
    border-radius: 30px;
    overflow: hidden;
  }
  .card--front {
    left: 71px;
    top: 28px;
    background: radial-gradient(ellipse at 58% 50%, var(--card-grey-light) 0%, var(--card-grey) 85%);
  }
  .card--back {
    left: 561px;
    top: 454px;
    background: var(--brand-orange);
  }
  .front-mark {
    position: absolute;
    left: -22px;
    top: 78px;
    width: 254px;
    height: 200px;
  }
  .front-name {
    position: absolute;
    left: 262px;
    top: 122px;
    width: 310px;
    text-align: center;
    color: var(--ink-dark);
    line-height: 1.1;
  }
  .front-name__line {
    display: block;
    font-size: 38px;
    letter-spacing: 1px;
  }
  .back-band {
    position: absolute;
    left: 134px;
    top: 66px;
    width: 310px;
    height: 52px;
    background: linear-gradient(90deg, var(--band-light) 0 38%, var(--band-dark) 38% 100%);
    display: flex;
    align-items: center;
    justify-content: center;
  }
  .back-band__name {
    color: var(--ink-dark);
    font-size: 21px;
    letter-spacing: 0.5px;
  }
  .contact {
    position: absolute;
    left: 34px;
    top: 162px;
    color: var(--text-light);
    font-size: 13.5px;
    line-height: 1.35;
    list-style: none;
  }
  .contact__item { margin-bottom: 20px; }
</style>
</head>
<body>
  <section class="card card--front" aria-label="Card front">
    <svg class="front-mark" viewBox="0 0 254 200" aria-hidden="true">
      <circle cx="127" cy="100" r="92" fill="#ececec" stroke="var(--brand-orange)" stroke-width="6"/>
    </svg>
    <h1 class="front-name">
      <span class="front-name__line">CORVELL</span>
      <span class="front-name__line">DESIGN HOUSE</span>
    </h1>
  </section>

  <section class="card card--back" aria-label="Card back">
    <div class="back-band">
      <span class="back-band__name">CORVELL DESIGN HOUSE</span>
    </div>
    <ul class="contact">
      <li class="contact__item">Address:- Suite 8, 42 - 48 Marlow Coast Road, Marlow,<br>WA 6100 PO Box: 2210 Marlow WA 6901</li>
      <li class="contact__item">Phone: 1300 00 27 41</li>
      <li class="contact__item">Reid Mobile: 0400 118 254</li>
      <li class="contact__item">Lena Mobile: 0400 552 903</li>
    </ul>
  </section>
</body>
</html>
```